Announcement for a New Trauma Therapy Group - Rack Card

I need a two-sided "rack" card that is 4x9 announcing a Women's Trauma and Loss Group. I am a licensed therapist and will be starting this support group for women who have experienced trauma of all kinds. In addition to groups, I offer individual, couples, and family counseling sessions.

I would like to see designs that are soft tones and use colors like muted blues, greens, and sand tones. The final design should communicate hope and healing as well as have a peaceful feel to it.

I would like a picture of a woman's profile from either the side or from behind her. (possibly a contemplative picture on a beach)

I am attaching a picture of myself to go alongside the bio information as well.

On One Side, I need the description of the group and contact info:

Healing the Hurting Heart
Women's Trauma & Loss Group
Led by Licensed Professional Counselor, Joy Belden Crane

10 Week Group
Cost - $35 session
Group size limited to 10 participants

Topics Include:
What is Trauma?
How Trauma Affects Us
Creating a Feeling of Safety
Managing Trauma Triggers
Importance of Self Care
Healthy vs. Unhealthy Coping
Guilt, Shame, and Blame
Victim vs. Victimized
Grieving through Loss
Anger and Forgiveness
Imagining a Better Future

For More Information, Contact:
Joy Belden Crane, LPC, LMFT
(555) 614-3928
joy@brightmeadowcare.example

On Side Two:

Life hurts and does not seem fair. So what do you do when you are faced with an event in your life that knocks you off your feet? It seems no one understands what you are feeling and no one knows just what to say. It is tempting to pull away and isolate or put up a mask and pretend everything is OK.

It is my desire you know that you are not alone! There are others who understand the feelings you are going through and offer a safe place for encouraging support. I want to invite you to embark on a courageous journey of healing where you will not only learn how to "survive" after trauma and loss, but instead, learn that you can once again "thrive"!
- Joy Belden Crane, LPC, LMFT

Joy Belden Crane is a Licensed Professional Counselor and Licensed Marriage and Family Therapist. She is the owner of Still Waters Counseling Services located in Tulsa, OK.

Joy is a trauma survivor herself and understands firsthand the unique challenges that can arise on the journey to healing.

(Include Joy's picture next to bio)

(Attach logo and business information to this side as well.)

Target Market(s)

Women who have gone through a traumatic experience or loss and are hurting emotionally

Industry/Entity Type

Counsellor

Font styles to use
Serif
Script

Colors
fbe7d2
86cfc6
cfeae6
85abd2
cfdeed

Requirements
Must have
• Joy's picture as well as her logo and contact information must be on the card.
• One side of the card should describe the group with the following description:
• "Healing the Hurting Heart"
• Women's Trauma & Loss Group
• Led by Licensed Professional Counselor, Joy Belden Crane
• 10 Week Group
• Cost - $35 session
• Group size limited to 10 participants
• Topics Include:
• What is Trauma?
• How Trauma Affects Us
• Creating a Feeling of Safety
• Managing Trauma Triggers
• Importance of Self Care
• Healthy vs. Unhealthy Coping
• Guilt, Shame, and Blame
• Victim vs. Victimized
• Grieving through Loss
• Anger and Forgiveness
• Imagining a Better Future
• For More Information, Contact:
• Joy Belden Crane, LPC, LMFT
• (555) 614-3928
• joy@brightmeadowcare.example
• On the second side, it must have this note from Joy:
• Life hurts and does not seem fair. So what do you do when you are faced with an event in your life that knocks you off your feet? It seems no one understands what you are feeling and no one knows just what to say. It is tempting to pull away and isolate or put up a mask and pretend everything is OK.
• It is my desire you know that you are not alone! There are others who understand the feelings you are going through and offer a safe place for encouraging support. I want to invite you to embark on a courageous journey of healing where you will not only learn how to "survive" after trauma and loss, but instead, learn that you can once again "thrive"!
• - Joy Belden Crane, LPC, LMFT
• Joy Belden Crane is a Licensed Professional Counselor and Licensed Marriage and Family Therapist. She is the owner of Still Waters Counseling Services located in Tulsa, OK.
• Joy is a trauma survivor herself and understands firsthand the unique challenges that can arise on the journey to healing. In addition to facilitating groups, Joy also offers individual, marriage, and family counseling.
Nice to have
• soft muted colors that are peaceful. Light blues, greens, sand colors would work well. A picture at the top of the card of either a woman or a woman's profile that is hopeful such as a woman sitting at a beach overlooking the ocean.
Should not have
• No harsh or bright bold colors. This card needs to have a peaceful feeling to it.

```html
<!DOCTYPE html>
<html lang="en">
<head>
<meta charset="utf-8">
<title>Healing the Hurting Heart – Rack Card</title>
<link href="https://fonts.googleapis.com/css2?family=Great+Vibes&family=Montserrat:wght@400;500;600;700&family=Source+Sans+3:wght@300;400&family=Oswald:wght@300;400&display=swap" rel="stylesheet">
<style>
:root{
  --page:#ececec;
  --ink:#1f1f1f;
  --blue:#7b9dc7;
  --blue-soft:#cfdeed;
  --teal:#86cfc6;
  --mint:#cfeae6;
  --mint-deep:#d3ece8;
  --sand:#fbe7d2;
  --white:#ffffff;
  --green:#4e8a2e;
}
*{box-sizing:border-box;margin:0;padding:0}
html,body{width:1200px;height:1200px;overflow:hidden;background:var(--page)}
body{position:relative;font-family:"Montserrat",sans-serif;color:var(--ink)}
.card{position:absolute;top:105px;width:440px;height:990px;overflow:hidden;background:var(--white);box-shadow:0 6px 18px rgba(0,0,0,.15)}
.card--front{left:130px}
.card--back{left:630px;background:linear-gradient(180deg,var(--mint-deep) 0%,var(--mint-deep) 62%,var(--white) 78%)}
.abs{position:absolute}

/* front */
.hero{left:0;top:0;width:440px;height:390px;background:linear-gradient(180deg,#bcd3ea 0%,#dde9f4 52%,#7d98ad 54%,#9fb2bf 86%,#c9b9a4 92%,#bcae9c 100%)}
.brand{display:flex;align-items:center;gap:8px;font-family:"Montserrat",sans-serif;font-weight:600;color:var(--green);white-space:nowrap}
.brand__dot{border-radius:50%;background:var(--green);flex:none}
.brand--hero{left:0;width:440px;top:84px;justify-content:center;font-size:22px}
.brand--hero .brand__dot{width:16px;height:16px}
.wave{left:0;width:440px}
.title{left:58px;top:400px;font-family:"Great Vibes",cursive;font-weight:400;font-size:44px;line-height:46px;color:var(--ink);white-space:nowrap}
.title span{display:block}
.title span+span{padding-left:72px}
.lede{left:0;width:440px;top:512px;text-align:center;font-size:14.5px;font-weight:500;line-height:19px}
.weeks{left:0;width:440px;top:576px;text-align:center;font-size:21px;font-weight:700;letter-spacing:.5px}
.cost{left:118px;top:606px;display:flex;font-size:18px;font-weight:500;height:26px}
.cost__label{background:var(--blue);color:var(--white);padding:0 16px;line-height:26px}
.cost__value{background:var(--mint);padding:0 10px;line-height:26px}
.limit{left:0;width:440px;top:638px;text-align:center;font-size:17.5px;font-weight:500}
.topics{left:22px;top:672px;width:396px;height:200px;border:1.5px solid var(--blue);border-radius:4px;background:var(--mint)}
.topics__tag{left:146px;top:660px;width:146px;height:24px;border-radius:12px;background:var(--blue);color:var(--white);font-family:"Source Sans 3",sans-serif;font-size:18px;text-align:center;line-height:24px}
.topics__cols{position:absolute;left:0;top:20px;width:100%;display:flex}
.topics__col{list-style:none;padding:0 4px 0 8px;font-family:"Source Sans 3",sans-serif;font-size:15px;line-height:18px}
.topics__col:first-child{width:202px;border-right:1px solid #b9d3cf}
.topics__col li{display:flex;gap:8px;margin-bottom:9.6px}
.topics__col li svg{flex:none;margin-top:5px}
.more{font-size:15px;font-weight:600;white-space:nowrap}
.card--front .more{left:0;width:440px;top:884px;text-align:center}
.band{left:0;width:440px;height:100px;top:890px}
.contact{color:var(--white);font-size:15px;line-height:23px;white-space:nowrap}
.contact b{font-weight:600}
.card--front .contact{left:0;width:440px;top:935px;text-align:center}
.contact__row{display:inline-flex;align-items:center;gap:5px;margin:0 4px}

/* back */
.quote{left:28px;top:34px;width:384px;height:326px;border:1.5px solid var(--blue);border-radius:6px}
.quote__mark{font-family:Georgia,serif;font-weight:700;font-size:58px;line-height:1;color:var(--blue);background:var(--mint-deep);padding:0 3px}
.quote__mark--open{left:36px;top:14px}
.quote__mark--close{left:370px;top:332px}
.quote__text{left:35px;top:52px;width:370px;font-size:12.6px;line-height:16.6px;text-align:justify}
.quote__text p+p{margin-top:17px}
.quote__sign{left:35px;width:370px;top:317px;text-align:right;font-size:12.6px}
.quote__sign i{font-weight:400}
.portrait{left:28px;top:383px;width:386px;height:225px;border-radius:6px;background:linear-gradient(180deg,#a7a08c 0%,#8c8a7f 30%,#9b8f82 60%,#6e6760 100%)}
.bio{left:35px;top:625px;width:370px;font-size:12.6px;line-height:16.6px;text-align:justify}
.bio p+p{margin-top:13px}
.biz{left:0;top:735px;width:440px;height:140px}
.brand--biz{left:60px;top:62px;font-size:15px}
.brand--biz .brand__dot{width:11px;height:11px}
.biz__rule{left:218px;top:0;width:1px;height:140px;background:var(--teal)}
.biz__name{left:236px;top:22px;font-family:"Oswald",sans-serif;font-weight:300;font-size:17px;white-space:nowrap}
.biz__list{left:248px;list-style:none;font-family:"Oswald",sans-serif;font-weight:300;font-size:9px;line-height:13px;white-space:nowrap}
.biz__list li::before{content:"";display:inline-block;width:3px;height:3px;border-radius:50%;background:var(--teal);margin-right:8px;vertical-align:middle}
.biz__list--cred{top:48px;color:var(--green)}
.biz__list--reach{top:100px;font-size:10.5px;line-height:14px}
.headshot{left:32px;top:855px;width:126px;height:126px;border-radius:50%;border:4px solid var(--teal);background:radial-gradient(circle at 50% 45%,#d8b98c 0%,#b98c56 55%,#3d4a55 100%);z-index:3}
.card--back .more{left:172px;top:885px;z-index:2}
.card--back .band{top:896px;height:94px}
.card--back .contact{left:175px;top:920px;font-size:14px;line-height:20px}
.contact__line{display:flex;align-items:center;gap:5px}
</style>
</head>
<body>

<section class="card card--front" aria-label="Front side">
  <div class="abs hero" role="img" aria-label="Photo of a woman seen from behind, sitting on a beach rock and looking out over a calm sea under a soft blue sky"></div>
  <div class="abs brand brand--hero"><span class="brand__dot"></span>Still Waters Counseling</div>

  <svg class="abs wave" style="top:360px" width="440" height="70" viewBox="0 0 440 70">
    <path d="M0 24 Q220 -6 440 30 L440 70 L0 70Z" fill="var(--teal)"/>
    <path d="M0 34 Q220 4 440 40 L440 70 L0 70Z" fill="var(--white)"/>
  </svg>

  <h1 class="abs title"><span>Healing the</span><span>Hurting Heart</span></h1>
  <p class="abs lede">Women's Trauma &amp; Loss Group Led by<br>Licensed Professional Counselor,<br>Joy Belden Crane</p>
  <p class="abs weeks">10 WEEK GROUP</p>
  <div class="abs cost"><span class="cost__label">COST</span><span class="cost__value">$35 session</span></div>
  <p class="abs limit">Group size limited to 10 participants</p>

  <div class="abs topics">
    <div class="topics__cols">
      <ul class="topics__col">
        <li><svg width="9" height="9" viewBox="0 0 9 9"><rect x=".5" y=".5" width="8" height="8" fill="none" stroke="var(--blue)"/><path d="M2 4.5l2 2 3-4" fill="none" stroke="var(--blue)"/></svg>What is Trauma?</li>
        <li><svg width="9" height="9" viewBox="0 0 9 9"><rect x=".5" y=".5" width="8" height="8" fill="none" stroke="var(--blue)"/><path d="M2 4.5l2 2 3-4" fill="none" stroke="var(--blue)"/></svg>How Trauma Affects Us</li>
        <li><svg width="9" height="9" viewBox="0 0 9 9"><rect x=".5" y=".5" width="8" height="8" fill="none" stroke="var(--blue)"/><path d="M2 4.5l2 2 3-4" fill="none" stroke="var(--blue)"/></svg>Creating a Feeling of Safety</li>
        <li><svg width="9" height="9" viewBox="0 0 9 9"><rect x=".5" y=".5" width="8" height="8" fill="none" stroke="var(--blue)"/><path d="M2 4.5l2 2 3-4" fill="none" stroke="var(--blue)"/></svg>Managing Trauma Triggers</li>
        <li><svg width="9" height="9" viewBox="0 0 9 9"><rect x=".5" y=".5" width="8" height="8" fill="none" stroke="var(--blue)"/><path d="M2 4.5l2 2 3-4" fill="none" stroke="var(--blue)"/></svg>Importance of Self Care</li>
        <li><svg width="9" height="9" viewBox="0 0 9 9"><rect x=".5" y=".5" width="8" height="8" fill="none" stroke="var(--blue)"/><path d="M2 4.5l2 2 3-4" fill="none" stroke="var(--blue)"/></svg>Healthy vs. Unhealthy<br>Coping</li>
      </ul>
      <ul class="topics__col">
        <li><svg width="9" height="9" viewBox="0 0 9 9"><rect x=".5" y=".5" width="8" height="8" fill="none" stroke="var(--blue)"/><path d="M2 4.5l2 2 3-4" fill="none" stroke="var(--blue)"/></svg>Guilt, Shame, and Blame</li>
        <li><svg width="9" height="9" viewBox="0 0 9 9"><rect x=".5" y=".5" width="8" height="8" fill="none" stroke="var(--blue)"/><path d="M2 4.5l2 2 3-4" fill="none" stroke="var(--blue)"/></svg>Victim vs. Victimized</li>
        <li><svg width="9" height="9" viewBox="0 0 9 9"><rect x=".5" y=".5" width="8" height="8" fill="none" stroke="var(--blue)"/><path d="M2 4.5l2 2 3-4" fill="none" stroke="var(--blue)"/></svg>Grieving through Loss</li>
        <li><svg width="9" height="9" viewBox="0 0 9 9"><rect x=".5" y=".5" width="8" height="8" fill="none" stroke="var(--blue)"/><path d="M2 4.5l2 2 3-4" fill="none" stroke="var(--blue)"/></svg>Anger and Forgiveness</li>
        <li><svg width="9" height="9" viewBox="0 0 9 9"><rect x=".5" y=".5" width="8" height="8" fill="none" stroke="var(--blue)"/><path d="M2 4.5l2 2 3-4" fill="none" stroke="var(--blue)"/></svg>Imagining a Better Future</li>
      </ul>
    </div>
  </div>
  <div class="abs topics__tag">Topics Include:</div>

  <p class="abs more">For More Information, Contact:</p>
  <svg class="abs band" width="440" height="100" viewBox="0 0 440 100">
    <path d="M0 0 Q220 28 440 6 L440 100 L0 100Z" fill="var(--teal)"/>
    <path d="M0 8 Q220 34 440 12 L440 100 L0 100Z" fill="var(--white)"/>
    <path d="M0 14 Q220 38 440 16 L440 100 L0 100Z" fill="var(--blue)"/>
  </svg>
  <div class="abs contact">
    <div><b>Joy Belden Crane,</b> LPC, LMFT</div>
    <div>
      <span class="contact__row"><svg width="11" height="11" viewBox="0 0 24 24"><path d="M6.6 10.8a15 15 0 006.6 6.6l2.2-2.2c.3-.3.7-.4 1-.2 1.1.4 2.3.6 3.6.6.6 0 1 .4 1 1V20c0 .6-.4 1-1 1A17 17 0 013 4c0-.6.4-1 1-1h3.5c.6 0 1 .4 1 1 0 1.3.2 2.5.6 3.6.1.3 0 .7-.2 1z" fill="var(--white)"/></svg><b>(555) 614-3928</b></span>
      <span class="contact__row"><svg width="11" height="9" viewBox="0 0 22 16"><rect width="22" height="16" rx="1" fill="var(--white)"/><path d="M1 1l10 8 10-8" fill="none" stroke="var(--blue)" stroke-width="1.6"/></svg>joy@brightmeadowcare.example</span>
    </div>
  </div>
</section>

<section class="card card--back" aria-label="Back side">
  <div class="abs quote"></div>
  <span class="abs quote__mark quote__mark--open">“</span>
  <div class="abs quote__text">
    <p>Life hurts and does not seem fair. So what do you do when you are faced with an event in your life that knocks you off your feet? It seems no one understands what you are feeling and no one knows just what to say. It is tempting to pull away and isolate or put up a mask and pretend everything is OK.</p>
    <p>It is my desire you know that you are not alone! There are others who understand the feelings you are going through and offer a safe place for encouraging support. I want to invite you to embark on a courageous journey of healing where you will not only learn how to "survive" after trauma and loss, but instead, learn that you can once again "thrive"!</p>
  </div>
  <p class="abs quote__sign">- <b>Joy Belden Crane</b>, <i>LPC, LMFT</i></p>
  <span class="abs quote__mark quote__mark--close">”</span>

  <div class="abs portrait" role="img" aria-label="Photo of the counselor sitting on a rock on a sandy beach at sunset"></div>

  <div class="abs bio">
    <p>Joy Belden Crane is a Licensed Professional Counselor and Licensed Marriage and Family Therapist. She is the owner of Still Waters Counseling Services located in Tulsa, OK.</p>
    <p>Joy is a trauma survivor herself and understands firsthand the unique challenges that can arise on the journey to healing.</p>
  </div>

  <div class="abs biz">
    <div class="abs brand brand--biz"><span class="brand__dot"></span>Still Waters</div>
    <div class="abs biz__rule"></div>
    <p class="abs biz__name">Joy Crane, LPC-S, LMFT</p>
    <ul class="abs biz__list biz__list--cred">
      <li>Licensed Professional Counselor</li>
      <li>Licensed Marriage and Family Therapist</li>
    </ul>
    <ul class="abs biz__list biz__list--reach">
      <li>555.614.3928</li>
      <li>joy@brightmeadowcare.example</li>
    </ul>
  </div>

  <div class="abs headshot" role="img" aria-label="Portrait photo of the counselor"></div>
  <p class="abs more">For More Information, Contact:</p>
  <svg class="abs band" width="440" height="94" viewBox="0 0 440 94">
    <path d="M0 4 Q220 12 440 0 L440 94 L0 94Z" fill="var(--teal)"/>
    <path d="M0 11 Q220 18 440 6 L440 94 L0 94Z" fill="var(--white)"/>
    <path d="M0 16 Q220 22 440 10 L440 94 L0 94Z" fill="var(--blue)"/>
  </svg>
  <div class="abs contact">
    <div><b>Joy Belden Crane,</b> LPC, LMFT</div>
    <div class="contact__line"><svg width="11" height="11" viewBox="0 0 24 24"><path d="M6.6 10.8a15 15 0 006.6 6.6l2.2-2.2c.3-.3.7-.4 1-.2 1.1.4 2.3.6 3.6.6.6 0 1 .4 1 1V20c0 .6-.4 1-1 1A17 17 0 013 4c0-.6.4-1 1-1h3.5c.6 0 1 .4 1 1 0 1.3.2 2.5.6 3.6.1.3 0 .7-.2 1z" fill="var(--white)"/></svg><b>(555) 614-3928</b></div>
    <div class="contact__line"><svg width="11" height="9" viewBox="0 0 22 16"><rect width="22" height="16" rx="1" fill="var(--white)"/><path d="M1 1l10 8 10-8" fill="none" stroke="var(--blue)" stroke-width="1.6"/></svg>joy@brightmeadowcare.example</div>
  </div>
</section>

</body>
</html>
```